Property development & Investment company Need a logo & business card design

Our name is KT Estates Australia Pty Ltd
Need logo & business card design

Target Market(s)

People dealing in commercial property

Industry/Entity Type

Business

Contact Information for Business Card

KT Estates Australia
Peter Moss Mobile0419 703 646
Email Peter@birchvale-sample.com.au

Font styles to use
Sans Serif

Requirements
Must have
• company name
• contact details
Nice to have
• KT Estates Bold
• Australia Not Bold
Should not have
• To busy of a look

```html
<!DOCTYPE html>
<html lang="en">
<head>
<meta charset="utf-8">
<title>KT Estates Australia – Business Card</title>
<link rel="stylesheet" href="https://fonts.googleapis.com/css2?family=Lato:wght@400;700&display=swap">
<style>
  :root {
    --brand-blue: #2157a3;
    --ink: #1d1d1f;
    --paper: #ffffff;
    --backdrop: #e9eaec;
  }
  * { margin: 0; padding: 0; box-sizing: border-box; }
  html, body {
    width: 1200px;
    height: 900px;
    overflow: hidden;
    background: var(--backdrop);
    font-family: "Lato", sans-serif;
  }
  .canvas {
    position: relative;
    width: 1200px;
    height: 900px;
  }
  .card {
    position: absolute;
    width: 580px;
    height: 330px;
    box-shadow: 0 6px 18px rgba(0,0,0,0.18);
  }
  .card--back {
    left: 520px;
    top: 90px;
    background: var(--brand-blue);
    display: flex;
    align-items: center;
    justify-content: center;
  }
  .card--front {
    left: 100px;
    top: 440px;
    background: var(--paper);
    overflow: hidden;
  }
  .wordmark {
    display: flex;
    align-items: center;
    gap: 12px;
    font-weight: 700;
    letter-spacing: -0.5px;
    white-space: nowrap;
  }
  .wordmark__dot {
    display: block;
    border-radius: 50%;
  }
  .card--back .wordmark {
    color: var(--paper);
    font-size: 44px;
  }
  .card--back .wordmark__dot {
    width: 22px;
    height: 22px;
    background: var(--paper);
  }
  .card--front .wordmark {
    position: absolute;
    left: 34px;
    top: 38px;
    color: var(--brand-blue);
    font-size: 30px;
  }
  .card--front .wordmark__dot {
    width: 16px;
    height: 16px;
    background: var(--brand-blue);
  }
  .contact {
    position: absolute;
    left: 250px;
    top: 150px;
    right: 40px;
    color: var(--ink);
  }
  .contact__name {
    color: var(--brand-blue);
    font-size: 26px;
    font-weight: 400;
    line-height: 1.1;
  }
  .contact__role {
    font-size: 17px;
    margin-bottom: 16px;
  }
  .contact__line {
    display: flex;
    align-items: center;
    gap: 12px;
    font-size: 17px;
    line-height: 1.6;
    white-space: nowrap;
  }
  .contact__icon {
    width: 16px;
    height: 16px;
    flex: none;
  }
  .card__band {
    position: absolute;
    left: 0;
    right: 0;
    bottom: 0;
    height: 12px;
    background: var(--brand-blue);
  }
</style>
</head>
<body>
<div class="canvas">
  <section class="card card--back" aria-label="Card back">
    <div class="wordmark"><span class="wordmark__dot"></span>KT Estates Australia</div>
  </section>

  <section class="card card--front" aria-label="Card front">
    <div class="wordmark"><span class="wordmark__dot"></span>KT Estates Australia</div>

    <div class="contact">
      <p class="contact__name">Peter Moss</p>
      <p class="contact__role">Manager</p>
      <p class="contact__line">
        <svg class="contact__icon" viewBox="0 0 16 16" aria-hidden="true">
          <rect x="4" y="1" width="8" height="14" rx="1.5" fill="none" stroke="#2157a3" stroke-width="1.5"/>
          <line x1="6.5" y1="12.5" x2="9.5" y2="12.5" stroke="#2157a3" stroke-width="1.2"/>
        </svg>
        0455 218 907
      </p>
      <p class="contact__line">
        <svg class="contact__icon" viewBox="0 0 16 16" aria-hidden="true">
          <rect x="1" y="3" width="14" height="10" fill="#2157a3"/>
          <polyline points="1,3 8,9 15,3" fill="none" stroke="#ffffff" stroke-width="1.2"/>
        </svg>
        Peter@birchvale-sample.com.au
      </p>
    </div>

    <div class="card__band"></div>
  </section>
</div>
</body>
</html>
```